Flyer: Bright Days, Open Doors

Please create a two (2) page flyer. We welcome minor updates/ changes to the Bright Days Open Doors flyer that is attached as a word document. We are aiming for the same general look and feel as the original PDF attached (please note that we have updated the content and would like the designers to use what is listed in the word document).
We encourage you to provide multiple versions using pictures of different people we have on hand. Our team currently likes how the lady in the picture is looking in the direction of the text - we encourage designers to please flip the photo if needed to make this possible. We also give the permission to crop the photos as needed to fit the design better aesthetically. In addition, the team wondered about having a pdf file that allows the user to easily change out the graphic between different photos to reflect different communities best—not sure if that is as easy as it sounds. Please remember to include the funding statement - you can find it within both of the current documents. For more information about our project, please visit https://velmorakin.org/open-doors/

```html
<!DOCTYPE html>
<html lang="en">
<head>
<meta charset="utf-8">
<title>Bright Days, Open Doors – Two-Page Flyer</title>
<link rel="stylesheet" href="https://fonts.googleapis.com/css2?family=Source+Sans+3:ital,wght@0,400;0,600;0,700;0,800;1,600&display=swap">
<style>
  :root{
    --maroon:#8a2f2a;
    --maroon-deep:#6e2420;
    --cream:#fbf4ec;
    --cream-2:#f4e6d9;
    --ink:#3b2b27;
    --teal:#9cc2bf;
    --terracotta:#c8684c;
    --backdrop:#e8e3dd;
  }
  *{box-sizing:border-box;margin:0;padding:0}
  html,body{width:1200px;height:900px;overflow:hidden}
  body{background:var(--backdrop);font-family:"Source Sans 3",Arial,sans-serif;color:var(--ink);position:relative}

  .page{position:absolute;top:80px;width:572px;height:740px;background:var(--cream);overflow:hidden;box-shadow:0 2px 10px rgba(0,0,0,.12)}
  .page--front{left:16px}
  .page--back{left:612px}

  /* shared */
  .banner{background:var(--maroon);color:#fff;font-weight:700;font-size:10.5px;letter-spacing:.02em;padding:5px 14px;border-radius:0 14px 14px 0;display:inline-block}
  .brand{display:flex;align-items:center;gap:7px;color:var(--maroon);font-weight:700;font-size:10px;line-height:1.1;text-transform:uppercase;white-space:nowrap}
  .brand__mark{width:22px;height:22px;border-radius:50%;background:var(--maroon);flex:none}
  .pulse{display:block}

  /* front page */
  .front__pattern{position:absolute;left:0;top:0;width:300px;height:420px;background:linear-gradient(160deg,#cfe2df 0%,#e7ded2 55%,var(--cream) 100%)}
  .front__photo{position:absolute;left:0;top:330px;width:300px;height:410px;background:linear-gradient(180deg,#d9c8bb 0%,#b98c80 40%,#b34a4a 75%,#e6cfd0 100%)}
  .front__brand{position:absolute;left:24px;top:46px}
  .front__title{position:absolute;right:26px;top:36px;text-align:right;color:var(--maroon);font-weight:800;font-size:38px;line-height:1.02}
  .front__col{position:absolute;left:236px;top:128px;width:316px;font-size:9.5px;line-height:1.3}
  .front__col .banner{margin-left:-6px;font-size:9.5px}
  .front__intro{margin:8px 0 10px;text-align:center;font-weight:600}
  .stats{display:flex;gap:10px;justify-content:center;margin-bottom:8px}
  .stat{display:flex;align-items:center;gap:5px}
  .stat__shape{width:26px;height:20px;background:var(--maroon);border-radius:3px;flex:none}
  .stat__shape--people{width:16px}
  .stat__num{color:var(--maroon);font-weight:800;font-size:22px;line-height:1;white-space:nowrap}
  .stat__label{font-size:7.5px;line-height:1.15;width:62px}
  .risk__head{color:var(--maroon);font-weight:800;font-size:13px;text-align:right;line-height:1.1;margin-bottom:4px}
  .risk__list{list-style:none;text-align:right;font-size:12px;line-height:1.45;margin-bottom:10px}
  .risk__list li::after{content:"";display:inline-block;width:8px;height:8px;border:1.5px solid var(--maroon);border-radius:50%;margin-left:6px;vertical-align:middle}
  .protect{list-style:none;text-align:right;margin-top:8px}
  .protect li{margin-bottom:4px}
  .protect li::after{content:"";display:inline-block;width:6px;height:6px;background:var(--terracotta);border-radius:50%;margin-left:6px;vertical-align:middle}
  .front__closing{color:var(--maroon);font-style:italic;font-weight:600;text-align:right;margin-top:6px}
  .front__footer{position:absolute;right:26px;bottom:22px;text-align:right;font-size:10px;line-height:1.3}
  .front__footer a{color:var(--ink);font-weight:700;text-decoration:none}

  /* back page */
  .back__photos{position:absolute;right:0;top:0;width:220px;height:520px}
  .back__photo{position:absolute;right:16px;width:170px;border-radius:6px}
  .back__photo--a{top:14px;height:170px;background:linear-gradient(160deg,#e9e1d9,#bfa89a)}
  .back__photo--b{top:190px;right:50px;height:150px;background:linear-gradient(160deg,#efe4da,#8d6a5c)}
  .back__photo--c{top:346px;height:160px;background:linear-gradient(160deg,#e6b4a6,#c8684c 50%,#a9b7c4)}
  .back__title{position:absolute;left:26px;top:28px;width:320px;color:var(--maroon);font-weight:800;font-size:16px;line-height:1.2}
  .back__intro{position:absolute;left:26px;top:74px;width:325px;font-size:9.5px;line-height:1.3}
  .back__intro p+p{margin-top:6px}
  .doctor{position:absolute;left:0;top:182px;width:340px;font-size:8.8px;line-height:1.25}
  .doctor .banner{margin-bottom:6px}
  .doctor__list{list-style:none;padding-left:26px}
  .doctor__item{display:flex;gap:8px;margin-bottom:6px}
  .doctor__icon{flex:none;width:16px;height:16px;border-radius:50%;background:var(--cream-2);border:1.5px solid var(--maroon)}
  .doctor__item strong{color:var(--maroon);font-weight:700}
  .doctor__item ul{list-style:disc;padding-left:12px}
  .steps{position:absolute;left:0;top:528px;width:390px;font-size:8.8px;line-height:1.25}
  .steps .banner{margin-bottom:5px}
  .steps ul{list-style:none;padding-left:26px}
  .steps li{margin-bottom:2px;padding-left:10px;position:relative}
  .steps li::before{content:"";position:absolute;left:0;top:4px;width:5px;height:5px;border-radius:50%;background:var(--terracotta)}
  .back__brand{position:absolute;right:22px;top:574px}
  .back__pulse{position:absolute;right:22px;top:608px}
  .funding{position:absolute;left:26px;right:26px;bottom:16px;font-size:6.8px;line-height:1.3}
</style>
</head>
<body>

<section class="page page--front">
  <div class="front__pattern" role="img" aria-label="Decorative geometric pattern in soft teal and sand tones"></div>
  <div class="front__photo" role="img" aria-label="Photo of an elder woman in a red blouse with a beaded necklace, looking toward the text"></div>

  <div class="brand front__brand"><span class="brand__mark"></span><span>Harrowgate Circle<br>for Elder Wellness</span></div>

  <h1 class="front__title">Bright Days,<br>Open Doors…</h1>

  <div class="front__col">
    <span class="banner">Keep Your Heart and Body Healthy to Protect Your Brain</span>
    <p class="front__intro">Everyone slows down as they get older, both in body and mind. Big changes in memory or thinking that make it hard to get through the day are not a normal part of aging. These changes could be signs of early dementia or Alzheimer's disease.</p>

    <div class="stats">
      <div class="stat"><span class="stat__shape"></span><span class="stat__num">1 in 9</span><span class="stat__label">People in the U.S. ages 65+ has Alzheimer's dementia</span></div>
      <div class="stat"><span class="stat__shape stat__shape--people"></span><span class="stat__num">1 in 3</span><span class="stat__label">American Indian people ages 65+ develops dementia</span></div>
    </div>

    <p class="risk__head">YOU ARE MORE AT RISK OF DEVELOPING<br>DEMENTIA IF YOU HAVE:</p>
    <ul class="risk__list">
      <li>High Blood Pressure</li>
      <li>Diabetes or</li>
      <li>You Smoke Cigarettes</li>
    </ul>

    <span class="banner">YOU CAN PROTECT YOUR BODY, HEART, AND MIND</span>
    <ul class="protect">
      <li>Schedule a "wellness" visit and health screenings every year with your doctor, even if you feel ok</li>
      <li>Keep a healthy blood pressure</li>
      <li>Be active or walk every day</li>
      <li>Maintain a healthy weight for your body size</li>
      <li>Eat a healthier diet with more fresh vegetables, fruits, whole grains, and fish</li>
      <li>Stop smoking cigarettes or chewing tobacco</li>
      <li>Get help managing your high blood pressure, diabetes, or to lose extra weight</li>
      <li>Talk to your doctor about how you feel because your mental health can affect your brain and physical health</li>
      <li>If it is hard for you to get through the day because of forgetfulness or memory problems, see your doctor right away</li>
    </ul>
    <p class="front__closing">You can do these things today to protect your mind and reduce the risk of or slow down dementia.</p>
  </div>

  <div class="front__footer">
    <svg class="pulse" width="150" height="18" viewBox="0 0 150 18" style="margin-left:auto"><polyline points="0,10 60,10 66,3 72,16 78,10 150,10" fill="none" stroke="var(--maroon)" stroke-width="1.2"/></svg>
    <p>For more information about our project, please visit</p>
    <a href="https://velmorakin.org/open-doors/">https://velmorakin.org/open-doors/</a>
  </div>
</section>

<section class="page page--back">
  <div class="back__photos">
    <div class="back__photo back__photo--a" role="img" aria-label="Portrait of a smiling elder woman with grey hair and glasses"></div>
    <div class="back__photo back__photo--b" role="img" aria-label="Portrait of a smiling middle-aged woman with dark hair"></div>
    <div class="back__photo back__photo--c" role="img" aria-label="Portrait of an elder man with glasses over a warm watercolor wash"></div>
  </div>

  <h2 class="back__title">The River of Life Flows Through Your Heart to Protect Your Mind and Body</h2>
  <div class="back__intro">
    <p>Your heart health plays a big part in the health of your brain. Your heart is like the start of a flowing river. Blood vessels that take blood to and from your heart are like connected streams that flow through your body. They feed your brain with oxygen and energy.</p>
    <p>You can do things to keep the streams freely flowing through your body, so your heart and brain stay strong and healthy.</p>
  </div>

  <div class="doctor">
    <span class="banner">WORKING WITH YOUR DOCTOR</span>
    <ul class="doctor__list">
      <li class="doctor__item"><span class="doctor__icon"></span><div><strong>Make an appointment</strong> for a "wellness" checkup with your doctor every year
        <ul><li>You will get tests and screenings to make sure you are healthy</li><li>They are usually free with Elder Care Plan B or the Tribal Wellness Service</li><li>If you have concerns about your memory, talk to your doctor</li></ul></div></li>
      <li class="doctor__item"><span class="doctor__icon"></span><div><strong>Have your blood pressure checked and know your numbers</strong>
        <ul><li>Your blood pressure should be less than 120/80 mmHg (120 over 80)</li><li>If you do not know how to take your blood pressure, ask your doctor to show you</li></ul></div></li>
      <li class="doctor__item"><span class="doctor__icon"></span><div><strong>Have your weight checked regularly and know your number.</strong> If you need to lose extra weight, ask your doctor about:
        <ul><li>The right number of calories for your body</li><li>Ideas for healthier food choices</li><li>Support for losing weight</li></ul></div></li>
      <li class="doctor__item"><span class="doctor__icon"></span><div><strong>If you smoke cigarettes or chew tobacco, ask about medicine, counseling, or help to stop</strong></div></li>
      <li class="doctor__item"><span class="doctor__icon"></span><div><strong>If you do not have diabetes,</strong> have your blood sugar level checked during your visit. Your blood sugar should be less than 100 mg/dL when you have not eaten.</div></li>
      <li class="doctor__item"><span class="doctor__icon"></span><div><strong>Talk with your doctor</strong> about all the medicines and vitamins you take. Your doctor can make sure they do not cause any problems with your memory, sleep, or brain function.</div></li>
    </ul>
  </div>

  <div class="steps">
    <span class="banner">OTHER STEPS YOU CAN TAKE</span>
    <ul>
      <li>Aim for 20 minutes of physical activity a day or 2 1/2 hours a week</li>
      <li>Eat less salt, sugar, red meat, and highly processed or packaged foods</li>
      <li>Read food labels to see how much salt (sodium) or fat is in your food</li>
      <li>Manage extra weight by making small changes. Losing a few pounds makes a difference</li>
      <li>Limit alcohol. No more than 1 drink per day for women and 2 for men</li>
      <li>Take your medicine for blood pressure, diabetes, and other problems even if you feel good</li>
      <li>Get at least seven hours of sleep each night. Talk to your doctor if you have trouble sleeping</li>
      <li>Keep your mind active. Visit with people in your community, help plan tribal events, go to your senior center, teach your language, play cards, or start a new hobby.</li>
    </ul>
  </div>

  <div class="brand back__brand"><span class="brand__mark"></span><span>Harrowgate Circle<br>for Elder Wellness</span></div>
  <svg class="pulse back__pulse" width="140" height="16" viewBox="0 0 140 16"><polyline points="0,9 60,9 65,2 70,14 75,9 140,9" fill="none" stroke="var(--maroon)" stroke-width="1.2"/></svg>

  <p class="funding">This product is supported by the Northvale Public Health Office (NPHO) of the Department of Community Wellbeing (DCW) as part of a financial assistance award totaling $348,711 with 100 percent funded by NPHO/DCW. The contents are those of the author(s) and do not necessarily represent the official views of, nor an endorsement, by NPHO/DCW, or the government.</p>
</section>

</body>
</html>
```